Business Card Design - Carrington Hill Lodge

We are looking at a new design for our business cards that has a modern and professional look. We run a residential aged care facility focussing on the care of residents. The cards will be used for potential clients, consultants and business opportunities in this sector. Blue and white is our main colours and would to see these colours incorporated in the design.
Industry/Entity Type
Business
Contact Information for Business Card
Carrington Hill Lodge, Darren Pelham, dpelham@carringtonhilllodge.com.au, Finance Manager, 0491 736 208, BCom, 48 Yarrabee Way, Kinross Vale, Qld 4132.

```html
<!DOCTYPE html>
<html lang="en">
<head>
<meta charset="UTF-8">
<title>Carrington Hill Lodge – Business Card</title>
<link rel="stylesheet" href="https://fonts.googleapis.com/css2?family=Open+Sans:wght@400;600;700&display=swap">
<style>
  :root {
    --page-bg: #e6e6e3;
    --card-white: #ffffff;
    --lodge-blue: #4a79a0;
    --accent-taupe: #a8968a;
    --edge-navy: #1f2d3d;
    --text-grey: #3f4448;
    --text-white: #ffffff;
  }
  html, body {
    margin: 0;
    padding: 0;
    width: 1200px;
    height: 873px;
    overflow: hidden;
    background: var(--page-bg);
    font-family: "Open Sans", Arial, sans-serif;
  }
  .sheet {
    width: 1200px;
    height: 873px;
    display: flex;
    align-items: center;
    justify-content: center;
    gap: 60px;
  }
  .card {
    width: 520px;
    height: 297px;
    display: block;
    box-shadow: 0 6px 18px rgba(0, 0, 0, 0.18);
  }
  .card-face { fill: var(--card-white); }
  .band { fill: var(--lodge-blue); }
  .band-edge-taupe { fill: none; stroke: var(--accent-taupe); stroke-width: 4; }
  .band-edge-navy { fill: none; stroke: var(--edge-navy); stroke-width: 1.2; }
  .brand-dot { fill: var(--lodge-blue); }
  .brand-name {
    fill: var(--lodge-blue);
    font-family: "Open Sans", Arial, sans-serif;
    font-weight: 700;
    letter-spacing: 0.6px;
  }
  .holder-name {
    fill: var(--lodge-blue);
    font-weight: 700;
    font-size: 13px;
  }
  .holder-title {
    fill: var(--text-grey);
    font-weight: 400;
    font-size: 10px;
  }
  .contact-text {
    fill: var(--text-white);
    font-weight: 400;
    font-size: 9.5px;
    letter-spacing: 0.2px;
  }
  .icon-disc { fill: var(--text-white); }
  .icon-glyph { fill: var(--lodge-blue); }
</style>
</head>
<body>
<main class="sheet">

  <svg class="card card-back" viewBox="0 0 520 297" xmlns="http://www.w3.org/2000/svg" aria-label="Card back">
    <rect class="card-face" width="520" height="297"/>
    <path class="band" d="M0,297 L0,240 C150,110 370,105 520,225 L520,297 Z"/>
    <path class="band-edge-taupe" d="M0,240 C150,110 370,105 520,225"/>
    <path class="band-edge-navy" d="M0,236 C150,106 370,101 520,221"/>

    <g class="brand">
      <circle class="brand-dot" cx="140" cy="88" r="22"/>
      <text class="brand-name" x="172" y="95" font-size="19">CARRINGTON HILL LODGE</text>
    </g>

    <g class="contact-line">
      <circle class="icon-disc" cx="152" cy="212" r="7"/>
      <rect class="icon-glyph" x="147.5" y="208.5" width="9" height="7" rx="1"/>
      <path d="M147.5,209 L152,213 L156.5,209" fill="none" stroke="#ffffff" stroke-width="1"/>
      <text class="contact-text" x="166" y="215.5">dpelham@carringtonhilllodge.com.au</text>
    </g>
  </svg>

  <svg class="card card-front" viewBox="0 0 520 297" xmlns="http://www.w3.org/2000/svg" aria-label="Card front">
    <rect class="card-face" width="520" height="297"/>
    <path class="band" d="M0,297 L0,255 C140,125 360,115 520,215 L520,297 Z"/>
    <path class="band-edge-taupe" d="M0,255 C140,125 360,115 520,215"/>
    <path class="band-edge-navy" d="M0,251 C140,121 360,111 520,211"/>

    <g class="brand">
      <circle class="brand-dot" cx="238" cy="48" r="19"/>
      <text class="brand-name" x="265" y="54" font-size="15">CARRINGTON HILL LODGE</text>
    </g>

    <g class="holder">
      <text class="holder-name" x="220" y="98">Carrington Hill Lodge, Darren Pelham</text>
      <text class="holder-title" x="220" y="114">Finance Manager</text>
    </g>

    <g class="contact-line phone">
      <circle class="icon-disc" cx="227" cy="196" r="7"/>
      <path class="icon-glyph" d="M224,191.5 l2,-0.5 l1.5,3 l-1.3,1 q1,2.4 3.2,3.4 l1,-1.3 l3,1.4 l-0.5,2 q-1,1 -2.6,0.6 q-5.6,-2 -7.2,-7.2 q-0.3,-1.5 0.9,-2.4 z"/>
      <text class="contact-text" x="241" y="199.5">0491 736 208</text>
    </g>

    <g class="contact-line address">
      <circle class="icon-disc" cx="227" cy="224" r="7"/>
      <path class="icon-glyph" d="M227,219 a3.6,3.6 0 0 1 3.6,3.6 q0,2.4 -3.6,6.4 q-3.6,-4 -3.6,-6.4 a3.6,3.6 0 0 1 3.6,-3.6 z"/>
      <circle cx="227" cy="222.6" r="1.3" fill="#ffffff"/>
      <text class="contact-text" x="241" y="227.5">48 Yarrabee Way, Kinross Vale, Qld 4132</text>
    </g>
  </svg>

</main>
</body>
</html>
```